Billboard Design

Billboard design featuring the colors dark teal and dark grey.
Company: Cedarbrook Hollow Properties
Services Real Estate & Management
Phone: 614-739-5081
Important info:
Professionalizing Property Management
Specialized training and credentials in Property Management
Serving single family, multifamily, complexes, and mixed use properties.

UPDATE: We have uploaded photos from a recent project of ours and would love to see them used on the billboard.

```html
<!DOCTYPE html>
<html lang="en">
<head>
<meta charset="utf-8">
<title>Cedarbrook Hollow Properties – Billboard</title>
<link href="https://fonts.googleapis.com/css2?family=Bebas+Neue&family=Crimson+Pro:wght@700&display=swap" rel="stylesheet">
<style>
  :root {
    --teal: #006d72;
    --teal-light: #3b989e;
    --ink: #000000;
    --grey: #58595b;
    --white: #ffffff;
    --stage-top: #444343;
    --stage-bottom: #121212;
  }
  * { margin: 0; padding: 0; box-sizing: border-box; }
  html, body { width: 1200px; height: 706px; overflow: hidden; }
  body {
    background: linear-gradient(180deg, var(--stage-top), var(--stage-bottom));
    font-family: "Crimson Pro", Georgia, serif;
  }
  .billboard {
    position: absolute;
    left: 76px; top: 88px;
    width: 1048px; height: 530px;
    overflow: hidden;
    background: var(--teal);
  }
  .billboard-shapes { position: absolute; inset: 0; }
  .headline {
    position: absolute;
    left: 465px; top: 27px;
    font-family: "Bebas Neue", Impact, sans-serif;
    font-size: 57px;
    line-height: 52px;
    color: var(--white);
    letter-spacing: 0.2px;
  }
  .tagline {
    position: absolute;
    left: 465px; top: 199px;
    font-size: 20.5px;
    line-height: 19px;
    color: var(--white);
  }
  .services {
    position: absolute;
    left: 464px; top: 257px;
    list-style: none;
    color: var(--white);
    font-size: 20px;
    line-height: 29px;
  }
  .services li { display: flex; align-items: center; gap: 10px; }
  .services svg { width: 20px; height: 20px; flex: none; }
  .brand-box {
    position: absolute;
    left: 457px; top: 428px;
    width: 248px; height: 82px;
    border: 2px solid var(--ink);
    background: var(--white);
    display: flex; align-items: center; justify-content: center;
    text-align: center;
    font-size: 21px;
    line-height: 22px;
    color: var(--ink);
  }
  .phone {
    position: absolute;
    left: 741px; top: 443px;
    display: flex; align-items: center; gap: 9px;
    color: var(--teal);
    font-size: 43px;
    line-height: 44px;
  }
  .phone svg { width: 40px; height: 40px; }
  .website {
    position: absolute;
    left: 737px; top: 490px;
    font-size: 16.5px;
    letter-spacing: 0.6px;
    color: var(--grey);
  }
</style>
</head>
<body>
<main class="billboard">
  <svg class="billboard-shapes" viewBox="0 0 1048 530" width="1048" height="530" aria-hidden="false">
    <defs>
      <linearGradient id="family-photo-tone" x1="0" y1="0" x2="1" y2="1">
        <stop offset="0" stop-color="#c9c3b4"/>
        <stop offset="0.45" stop-color="#8a9aa8"/>
        <stop offset="0.8" stop-color="#7f9a62"/>
        <stop offset="1" stop-color="#e9e6e2"/>
      </linearGradient>
      <linearGradient id="interior-tone" x1="0" y1="0" x2="0" y2="1">
        <stop offset="0" stop-color="#e4e4e2"/>
        <stop offset="0.6" stop-color="#b9b8b4"/>
        <stop offset="1" stop-color="#6f665c"/>
      </linearGradient>
    </defs>
    <rect class="photo-family" x="0" y="0" width="420" height="530" fill="url(#family-photo-tone)" role="img" aria-label="Photo of a smiling couple in front of their home with a white picket fence"/>
    <path class="band-light" d="M327,0 C410,150 430,380 352,530 L1048,530 L1048,0 Z" fill="var(--teal-light)"/>
    <path class="band-dark" d="M360,0 C452,150 462,380 366,530 L1048,530 L1048,0 Z" fill="var(--ink)"/>
    <path class="panel" d="M372,0 C478,150 488,380 400,530 L1048,530 L1048,0 Z" fill="var(--teal)"/>

    <circle cx="938" cy="83" r="119" fill="var(--white)"/>
    <circle cx="938" cy="83" r="115" fill="url(#interior-tone)" role="img" aria-label="Project photo: renovated kitchen with stainless steel appliances"/>
    <circle cx="964" cy="245" r="104" fill="var(--white)"/>
    <circle cx="964" cy="245" r="100" fill="url(#interior-tone)" role="img" aria-label="Project photo: open living room with vinyl plank floor"/>
    <circle cx="841" cy="309" r="92" fill="var(--white)"/>
    <circle cx="841" cy="309" r="88" fill="url(#interior-tone)" role="img" aria-label="Project photo: hallway with white doors"/>

    <path class="footer" d="M420,412 Q650,372 1048,420 L1048,530 L398,530 Z" fill="var(--white)"/>
    <path class="footer-stripe" d="M432,420 Q660,388 1048,428 L1048,442 Q660,400 428,434 Z" fill="var(--grey)"/>
  </svg>

  <h1 class="headline">Professionalizing<br>Property<br>Management</h1>
  <p class="tagline">Specialized training and credentials<br>in Property Management</p>

  <ul class="services">
    <li><svg viewBox="0 0 20 20"><circle cx="10" cy="10" r="8.5" fill="none" stroke="currentColor" stroke-width="2"/><path d="M5.5 10.2l3.2 3.2 6.5-7" fill="none" stroke="currentColor" stroke-width="2.4"/></svg>SINGLE FAMILY</li>
    <li><svg viewBox="0 0 20 20"><circle cx="10" cy="10" r="8.5" fill="none" stroke="currentColor" stroke-width="2"/><path d="M5.5 10.2l3.2 3.2 6.5-7" fill="none" stroke="currentColor" stroke-width="2.4"/></svg>MULTI FAMILY</li>
    <li><svg viewBox="0 0 20 20"><circle cx="10" cy="10" r="8.5" fill="none" stroke="currentColor" stroke-width="2"/><path d="M5.5 10.2l3.2 3.2 6.5-7" fill="none" stroke="currentColor" stroke-width="2.4"/></svg>COMPLEXES</li>
    <li><svg viewBox="0 0 20 20"><circle cx="10" cy="10" r="8.5" fill="none" stroke="currentColor" stroke-width="2"/><path d="M5.5 10.2l3.2 3.2 6.5-7" fill="none" stroke="currentColor" stroke-width="2.4"/></svg>MIXED USE PROPERTIES</li>
  </ul>

  <div class="brand-box">Cedarbrook Hollow<br>Properties</div>

  <div class="phone">
    <svg viewBox="0 0 40 40"><circle cx="20" cy="20" r="17" fill="none" stroke="currentColor" stroke-width="3.5"/><path d="M13 11.5c1-1 2.2-1 2.8 0l2 3c.5.8.3 1.6-.4 2.2l-1 .9c.9 2.2 2.7 4 4.9 5l.9-1c.6-.7 1.4-.9 2.2-.4l3 2c1 .6 1 1.8 0 2.8l-1.3 1.3c-1.2 1.2-3 1.3-5 .3-4.5-2.3-7.6-5.4-9.8-9.8-1-2-.9-3.8.3-5z" fill="currentColor"/></svg>
    <span class="phone-number">614-739-5081</span>
  </div>
  <p class="website">www.cedarbrookhollowproperties.com</p>
</main>
</body>
</html>
```